Kestrel Summit 2019 Enemies of the End-Times Church Flyer

We want a church conference flyer designed. We are looking for a professional, yet catchy design that uses our brand colors and logo creatively while communicating key information of the event effectively. <br/>The flyer must include all of the following:<br/>Title: Kestrel Summit 2019<br/>Topic: The Enemies of The End-Times Church <br/>Subtitles: <br/> -How the antichrist raises an army by social behavior engineering. <br/>-How the architects of modern social constructs escaped the church's radar. <br/>-The Holy Spirit's end-times agenda:<br/> The Knock-Out Punch!<br/>Speaker: Prophet Marcus Toliver <br/>Dates/time: December 27, 28 & 29 at 6pm<br/>Location: Halvorn Community Center <br/> 241 Pellham Street <br/> Portland, ME 04102<br/>Contact info: phone: 207-555-0148 <br/>email: contact@brookmeadow.example <br/> www.vutel.example<br/>*The flyer must also include a picture of the speaker and our Vutel logo <br/>Thanks, we look forward to seeing what you come up with!

Colors

Designer to choose colors to be used in the design.

Requirements
Must have
• The flyer must include all of the following:
• Title: Kestrel Summit 2019
• Topic: The Enemies of The End-Times Church
• Subtitles:
• -How the antichrist raises an army by social behavior engineering.
• -How the architects of modern social constructs escaped the church's radar.
• -The Holy Spirit's end-times agenda:
• The Knock-Out Punch!
• Speaker: Prophet Marcus Toliver
• Dates/time: December 27, 28 & 29 at 6pm
• Location: Halvorn Community Center
• 241 Pellham Street
• Portland, ME 04102
• Contact info: phone: 207-555-0148
• email: contact@brookmeadow.example
• www.vutel.example
• *The flyer must also include a picture of the speaker and our Vutel logo
Should not have
• Pictures of crosses or church buildings

```html
<!DOCTYPE html>
<html lang="en">
<head>
<meta charset="utf-8">
<title>Kestrel Summit 2019 – Flyer</title>
<link rel="stylesheet" href="https://fonts.googleapis.com/css2?family=Oswald:wght@500;700&family=Montserrat:wght@400;600;700;800&display=swap">
<style>
  :root {
    --crimson: #d9325f;
    --rose: #e04a72;
    --plum: #6a2a4f;
    --teal-dark: #16323c;
    --teal: #23505a;
    --navy: #1d3f8a;
    --yellow: #f7ec1b;
    --ink: #111111;
    --white: #ffffff;
    --stage: #e9eaec;
  }
  * { box-sizing: border-box; margin: 0; padding: 0; }
  html, body {
    width: 1200px; height: 901px; overflow: hidden;
    background: var(--stage);
  }
  .flyer {
    position: absolute; left: 30px; top: 83px;
    width: 1140px; height: 735px; overflow: hidden;
    background: linear-gradient(100deg, var(--crimson) 0%, var(--rose) 28%, var(--plum) 55%, var(--teal) 78%, var(--teal-dark) 100%);
    font-family: "Montserrat", sans-serif;
    color: var(--white);
  }
  .flyer__shapes { position: absolute; inset: 0; }
  .speaker-photo {
    position: absolute; left: 470px; top: 120px; width: 320px; height: 615px;
    background: linear-gradient(180deg, #2b2a33 0%, #1b1a22 60%, #121218 100%);
    border-radius: 160px 160px 0 0;
    opacity: .92;
  }
  .accent-bar {
    position: absolute; left: 0; top: 355px; width: 12px; height: 300px;
    background: var(--navy);
  }
  .title {
    position: absolute; left: 60px; top: 58px;
    font-family: "Oswald", sans-serif; font-weight: 700;
    text-transform: uppercase; line-height: .98;
  }
  .title__name { font-size: 62px; display: block; }
  .title__year { font-size: 96px; display: block; }
  .topic {
    position: absolute; left: 60px; top: 345px;
    font-family: "Oswald", sans-serif; font-weight: 700;
    text-transform: uppercase; line-height: 1;
  }
  .topic__lead { font-size: 34px; display: block; }
  .topic__main { font-size: 58px; display: block; }
  .points {
    position: absolute; left: 60px; top: 462px; width: 400px;
    list-style: none; font-size: 17px; line-height: 1.3;
  }
  .points li { margin-bottom: 10px; padding-left: 16px; position: relative; }
  .points li::before { content: "•"; position: absolute; left: 0; }
  .brand {
    position: absolute; right: 40px; top: 34px;
    display: flex; align-items: center; gap: 10px;
    font-family: "Montserrat", sans-serif; font-weight: 800; font-size: 34px;
    text-transform: uppercase; letter-spacing: 1px;
  }
  .brand__dot { width: 18px; height: 18px; border-radius: 50%; background: var(--crimson); }
  .details {
    position: absolute; left: 810px; top: 235px; width: 320px;
  }
  .label {
    font-size: 13px; font-weight: 700; text-transform: uppercase;
    color: var(--yellow); display: block;
  }
  .label--white { color: var(--white); }
  .speaker-name {
    font-family: "Oswald", sans-serif; font-weight: 700; font-size: 38px;
    line-height: 1.02; text-transform: uppercase; margin: 4px 0 22px;
  }
  .band {
    background: var(--yellow); color: var(--ink);
    font-weight: 800; text-transform: uppercase;
    padding: 6px 12px; margin: 5px 0 14px -12px;
    white-space: nowrap; width: max-content;
  }
  .band--date { font-size: 15px; }
  .band--phone { font-size: 24px; }
  .band--web { font-size: 13px; text-transform: none; margin-left: 0; }
  .address { font-size: 13px; line-height: 1.4; margin: 4px 0 14px; }
  .address strong { font-weight: 700; }
  .email { font-size: 13px; margin: 0 0 4px; }
</style>
</head>
<body>
  <main class="flyer">
    <svg class="flyer__shapes" width="1140" height="735" viewBox="0 0 1140 735" aria-hidden="true">
      <polygon points="290,230 790,170 560,620" fill="none" stroke="#ff6f9b" stroke-width="6"/>
    </svg>

    <div class="speaker-photo" role="img" aria-label="Portrait of the speaker, Prophet Marcus Toliver, seated in a dark suit"></div>

    <svg class="flyer__shapes" width="1140" height="735" viewBox="0 0 1140 735" aria-hidden="true">
      <line x1="290" y1="230" x2="470" y2="208" stroke="#ff6f9b" stroke-width="6"/>
    </svg>

    <div class="accent-bar"></div>

    <h1 class="title">
      <span class="title__name">Kestrel<br>Summit</span>
      <span class="title__year">2019</span>
    </h1>

    <h2 class="topic">
      <span class="topic__lead">The Enemies of the End-</span>
      <span class="topic__main">Times Church</span>
    </h2>

    <ul class="points">
      <li>How the antichrist raises an army by social behavior engineering</li>
      <li>How the architects of modern social constructs escaped the church's radar</li>
      <li>The Holy Spirit's end-times agenda:</li>
      <li>The Knock-Out Punch!</li>
    </ul>

    <div class="brand"><span class="brand__dot"></span>Vutel</div>

    <section class="details">
      <span class="label label--white">Speaker:</span>
      <p class="speaker-name">Prophet<br>Marcus Toliver</p>

      <span class="label">Dates/Time:</span>
      <p class="band band--date">December 27, 28 &amp; 29 at 6pm</p>

      <span class="label">Location:</span>
      <p class="address"><strong>Halvorn Community Center</strong><br>241 Pellham Street, Portland, ME 04102</p>

      <span class="label">Contact Us:</span>
      <p class="band band--phone">207-555-0148</p>
      <p class="email">contact@brookmeadow.example</p>
      <p class="band band--web">www.vutel.example</p>
    </section>
  </main>
</body>
</html>
```